8 x 8 Social Media Design - Tax, Accounting & Bookkeeping Service

Bright Ledger Advisory Group, Inc.

Tax, Accounting and Bookkeeping Services

“We provide our services, with you next mortgage in mind”

Special pricing available for all Mortgage Loan Customers!!

President / CEO Marcus Delaney

Primary service provider with over 27 years of experience

Call directly for more information: (555) 284-9037

Or email at: mdelaney@brightledgerhq.example

```html
<!DOCTYPE html>
<html lang="en">
<head>
<meta charset="utf-8">
<title>Bright Ledger Advisory Group – Tax, Accounting and Bookkeeping Services</title>
<link rel="stylesheet" href="https://fonts.googleapis.com/css2?family=Bebas+Neue&family=Poppins:ital,wght@0,500;0,600;0,700;1,700&display=swap">
<style>
  :root {
    --mat: #6a6a6a;
    --navy: #16427a;
    --navy-deep: #173d73;
    --gold: #b09f36;
    --white: #ffffff;
    --ink: #111111;
    --photo-light: #e9eef3;
    --photo-mid: #c9d3dd;
  }
  * { margin: 0; padding: 0; box-sizing: border-box; }
  html, body { width: 1200px; height: 1165px; overflow: hidden; background: var(--mat); }
  .post {
    position: absolute; left: 167px; top: 149px; width: 866px; height: 866px;
    background: var(--white); overflow: hidden;
    font-family: "Poppins", sans-serif;
  }
  .hero-photo {
    position: absolute; left: 380px; top: 0; width: 486px; height: 435px;
    background: linear-gradient(90deg, rgba(255,255,255,1) 0%, rgba(233,238,243,0.7) 35%, var(--photo-mid) 100%);
  }
  .headline {
    position: absolute; left: 37px; top: 38px;
    font-family: "Bebas Neue", sans-serif; font-size: 109px; line-height: 93px;
    color: var(--navy); letter-spacing: 0.5px;
  }
  .headline .accent { color: var(--gold); display: block; }
  .headline span { display: block; }
  .tagline-band {
    position: absolute; left: 0; top: 342px; width: 515px; height: 94px;
    background: var(--gold); border-top-right-radius: 32px;
    padding: 16px 0 0 39px;
    color: var(--white); font-weight: 600; font-size: 24px; line-height: 33px;
  }
  .offer-panel {
    position: absolute; left: 0; top: 435px; width: 866px; height: 300px;
    background: linear-gradient(100deg, var(--navy-deep) 0%, var(--navy) 60%, #1c4885 100%);
  }
  .offer {
    position: absolute; left: 39px; top: 21px;
    color: var(--white); font-weight: 600; font-size: 24px; line-height: 33px;
  }
  .presenter {
    position: absolute; left: 39px; top: 128px; height: 137px;
    border-left: 4px solid var(--gold); padding-left: 13px; color: var(--white);
  }
  .presenter .role { font-weight: 500; font-size: 26px; line-height: 30px; }
  .presenter .name { font-weight: 700; font-style: italic; font-size: 37px; line-height: 46px; color: var(--gold); }
  .presenter .bio { font-weight: 600; font-size: 22px; line-height: 29px; margin-top: 6px; }
  .portrait-frame { position: absolute; left: 0; top: 0; width: 866px; height: 866px; pointer-events: none; }
  .portrait {
    position: absolute; left: 484px; top: 482px; width: 382px; height: 384px;
    background: linear-gradient(180deg, #d9dde2 0%, #c9ccd1 45%, #2a2a2e 70%, #141416 100%);
    border-top-left-radius: 18px; border-top-right-radius: 18px;
  }
  .contact { position: absolute; left: 39px; top: 763px; }
  .contact-row { display: flex; align-items: center; gap: 9px; }
  .contact-row svg { flex: none; }
  .phone { font-weight: 700; font-size: 30px; line-height: 38px; color: var(--ink); }
  .email { font-weight: 500; font-size: 15px; line-height: 26px; color: var(--ink); }
  .brand {
    position: absolute; left: 322px; top: 738px; width: 132px;
    text-align: center; font-weight: 600; font-size: 13px; line-height: 17px; color: var(--navy);
  }
</style>
</head>
<body>
<main class="post">
  <div class="hero-photo" role="img" aria-label="Photo of hands working a calculator and writing over financial reports"></div>

  <h1 class="headline">
    <span>Tax, Accounting</span>
    <span class="accent">And Bookkeeping</span>
    <span>Services</span>
  </h1>

  <p class="tagline-band">We Provide Our Services,<br>With You Next Mortgage In Mind</p>

  <section class="offer-panel">
    <p class="offer">Special Pricing Available For<br>All Mortgage Loan Customers!!</p>
    <div class="presenter">
      <p class="role">President / CEO</p>
      <p class="name">Marcus Delaney</p>
      <p class="bio">Primary Service Provider with<br>Over 27 Years Of Experience</p>
    </div>
  </section>

  <div class="portrait" role="img" aria-label="Portrait photo of the president in a dark suit and tie"></div>

  <svg class="portrait-frame" viewBox="0 0 866 866" aria-hidden="true">
    <path d="M514 723 V527 Q514 513 528 513 H570" fill="none" stroke="var(--gold)" stroke-width="4"/>
    <path d="M702 513 H772 Q786 513 786 527 V680" fill="none" stroke="var(--gold)" stroke-width="4"/>
  </svg>

  <div class="contact">
    <div class="contact-row">
      <svg width="24" height="24" viewBox="0 0 24 24" aria-hidden="true">
        <circle cx="12" cy="12" r="12" fill="var(--gold)"/>
        <rect x="8" y="5" width="8" height="14" rx="2" fill="none" stroke="var(--white)" stroke-width="1.8"/>
        <circle cx="12" cy="16" r="1" fill="var(--white)"/>
      </svg>
      <span class="phone">(555) 284-9037</span>
    </div>
    <div class="contact-row">
      <svg width="24" height="24" viewBox="0 0 24 24" aria-hidden="true">
        <circle cx="12" cy="12" r="12" fill="var(--gold)"/>
        <rect x="6" y="8" width="12" height="9" rx="1" fill="none" stroke="var(--white)" stroke-width="1.8"/>
        <path d="M6.5 8.5 L12 13 L17.5 8.5" fill="none" stroke="var(--white)" stroke-width="1.8"/>
      </svg>
      <span class="email">mdelaney@brightledgerhq.example</span>
    </div>
  </div>

  <p class="brand">Bright Ledger Advisory Group, Inc.</p>
</main>
</body>
</html>
```